Lantern Hill Publicity is a new boutique Press Office with a small roster of well-chosen clients across an array of disciplines; from Art and Technology to Restaurants and Fashion. Based in Greenpoint Brooklyn, Lantern Hill Publicity achieves outstanding results through hard work, tenacity, efficiency and a sense of humor. We need a simple, versatile and classic design. We would like each side of the card to be white text on a black background.

Boutique

```html
<!DOCTYPE html>
<html lang="en">
<head>
<meta charset="utf-8">
<title>Lantern Hill Publicity – Business Card</title>
<link rel="stylesheet" href="https://fonts.googleapis.com/css2?family=Libre+Baskerville:wght@400;700&display=swap">
<style>
  :root {
    --page: #ffffff;
    --card: #000000;
    --panel: #111111;
    --divider: #474747;
    --rule: #8a8a8a;
    --ink: #ffffff;
  }
  * { margin: 0; padding: 0; box-sizing: border-box; }
  html, body {
    width: 1199px;
    height: 1200px;
    overflow: hidden;
    background: var(--page);
  }
  .canvas {
    position: relative;
    width: 1199px;
    height: 1200px;
    font-family: "Libre Baskerville", Georgia, serif;
    color: var(--ink);
  }
  .card {
    position: absolute;
    left: 214px;
    width: 772px;
    height: 535px;
    background: var(--card);
    overflow: hidden;
  }
  .card--front { top: 38px; }
  .card--back { top: 627px; }

  .wordmark {
    position: absolute;
    left: 0;
    right: 0;
    text-align: center;
    font-weight: 400;
    font-size: 30px;
    line-height: 1.45;
    letter-spacing: 0.22em;
    text-transform: uppercase;
    color: var(--ink);
  }
  .card--front .wordmark { top: 130px; }
  .card--back .wordmark { top: 230px; font-size: 34px; }

  .divider {
    position: absolute;
    left: 0;
    top: 330px;
    width: 100%;
    height: 10px;
    background: var(--divider);
  }
  .info-panel {
    position: absolute;
    left: 0;
    top: 340px;
    width: 100%;
    height: 195px;
    background: var(--panel);
  }
  .person {
    position: absolute;
    left: 27px;
    top: 30px;
  }
  .person__name {
    font-weight: 700;
    font-size: 27px;
    letter-spacing: -0.04em;
    line-height: 1;
  }
  .person__role {
    margin-top: 20px;
    font-weight: 700;
    font-size: 21px;
    letter-spacing: -0.04em;
    line-height: 1;
  }
  .contact-rule {
    position: absolute;
    left: 451px;
    top: 12px;
    width: 2px;
    height: 165px;
    background: var(--rule);
  }
  .contact {
    position: absolute;
    left: 466px;
    top: 20px;
    list-style: none;
    font-size: 19px;
    line-height: 30px;
    letter-spacing: -0.03em;
    white-space: nowrap;
  }
</style>
</head>
<body>
<main class="canvas">
  <section class="card card--front">
    <p class="wordmark">Lantern Hill<br>Publicity</p>
    <div class="divider"></div>
    <div class="info-panel">
      <div class="person">
        <p class="person__name">NAME</p>
        <p class="person__role">DESIGNATION</p>
      </div>
      <div class="contact-rule"></div>
      <ul class="contact">
        <li>Address line 1 Address line 1</li>
        <li>Millbrook, Eastfield</li>
        <li>http://www.lanternhillpr.com</li>
        <li>P: XXX-XXX-XXXX</li>
        <li>F: XXX-XXX-XXXX</li>
      </ul>
    </div>
  </section>

  <section class="card card--back">
    <p class="wordmark">Lantern Hill<br>Publicity</p>
  </section>
</main>
</body>
</html>
```